Dietitian needs a new business card design

I need a new business card design for my nutrition business that provides individual clinical nutrition advice for people with medical conditions. Business cards will be handed out to doctors, specialists and clients so will need to be sharp and project an image of professionalism

Target Market(s)

My clients are typically referred by doctors or specialists and the card will be used to handout to clients and their doctors.

Industry/Entity Type

Medical

Contact Information for Business Card

The business card will require the details below. These details can be found from my website https://www.kelvarrowclinic.com.au/

Font styles to use
Serif

Colors

Designer to choose colors to be used in the design.

Requirements
Must have
• 1. It needs be professional and contemporary
• 2. It needs to incorporate my logo
• 3. It needs space to write appointment times and dates
• 4. It needs to provide my phone number, fax number, email address and my web address
Nice to have
• Include the Registered Tovance Clinician Logo
• I have access to Framellow if required
• The locations I practise from
Should not have
• Pictures of food
• Spelling MIstakes

```html
<!DOCTYPE html>
<html lang="en">
<head>
<meta charset="utf-8">
<title>Kelvarrow Nutrition &amp; Dietetics – Business Card</title>
<link href="https://fonts.googleapis.com/css2?family=Open+Sans:wght@400;600;700&display=swap" rel="stylesheet">
<style>
  :root {
    --page-bg: #e6e8ea;
    --card-bg: #fbfbfb;
    --brand-blue: #1479c9;
    --deep-blue: #1559a8;
    --lime: #a6cc2e;
    --text-grey: #6b6f73;
    --rule-grey: #9a9ea2;
    --badge-orange: #f5a21e;
    --white: #ffffff;
  }
  * { box-sizing: border-box; margin: 0; padding: 0; }
  html, body {
    width: 1200px; height: 840px; overflow: hidden;
    background: var(--page-bg);
    font-family: "Open Sans", Arial, sans-serif;
  }
  .sheet {
    width: 1200px; height: 840px;
    display: flex; flex-direction: column; align-items: center; justify-content: center;
    gap: 36px;
  }
  .card {
    position: relative;
    width: 580px; height: 354px;
    background: var(--card-bg);
    box-shadow: 0 2px 10px rgba(0,0,0,0.12);
    overflow: hidden;
  }

  /* ---------- Appointment side ---------- */
  .badge {
    position: absolute; left: 0; top: 56px;
    width: 118px; height: 52px;
    background: var(--badge-orange);
    display: flex; align-items: center; justify-content: space-between;
    padding: 0 8px 0 10px;
  }
  .badge-text { color: var(--white); font-size: 8.5px; line-height: 1.2; width: 62px; }
  .badge-mark { width: 34px; height: 34px; border-radius: 50%; background: var(--white); }
  .appt-brand {
    position: absolute; top: 26px; left: 0; right: 0;
    display: flex; align-items: center; justify-content: center; gap: 10px;
  }
  .brand-dot { width: 30px; height: 30px; border-radius: 50%; background: var(--brand-blue); flex: none; }
  .brand-name { color: var(--brand-blue); font-weight: 600; font-size: 17px; white-space: nowrap; }
  .appt-tagline {
    position: absolute; top: 70px; left: 0; right: 0; text-align: center;
    color: var(--text-grey); font-size: 13px; line-height: 1.35;
  }
  .appt-rows {
    position: absolute; left: 64px; right: 40px; top: 150px;
    display: flex; flex-direction: column; gap: 34px;
  }
  .appt-row { display: flex; align-items: flex-end; color: var(--text-grey); font-size: 13px; }
  .appt-line { border-bottom: 1px solid var(--rule-grey); height: 1px; margin: 0 8px 4px; }
  .appt-line.date { width: 190px; }
  .appt-line.time { width: 110px; }

  /* ---------- Contact side ---------- */
  .side-band {
    position: absolute; left: 56px; top: 0; width: 92px; height: 354px;
    background: var(--brand-blue);
  }
  .side-band-top {
    position: absolute; left: 56px; top: 0; width: 92px; height: 126px;
    background: var(--lime);
  }
  .contact-mark {
    position: absolute; left: 70px; top: 100px;
    width: 52px; height: 52px; border-radius: 50%;
    background: var(--brand-blue); border: 3px solid var(--white);
  }
  .contact-brand-name {
    position: absolute; left: 160px; top: 112px;
    color: var(--brand-blue); font-weight: 600; font-size: 17px; white-space: nowrap;
  }
  .person { position: absolute; right: 34px; top: 38px; text-align: right; }
  .person-name { color: var(--deep-blue); font-weight: 700; font-size: 21px; line-height: 1.3; }
  .person-title { color: var(--lime); font-size: 14px; line-height: 1.3; }
  .icon { position: absolute; display: block; }
  .details {
    position: absolute; left: 172px; top: 168px;
    color: var(--text-grey); font-size: 13.5px; line-height: 18.6px;
  }
  .details .group + .group { margin-top: 16px; }
</style>
</head>
<body>
<main class="sheet">

  <section class="card card-appointment">
    <div class="badge">
      <span class="badge-text">Registered Tovance Clinician</span>
      <span class="badge-mark"></span>
    </div>
    <div class="appt-brand">
      <span class="brand-dot"></span>
      <span class="brand-name">Kelvarrow Nutrition &amp; Dietetics</span>
    </div>
    <p class="appt-tagline">Dietitian for Kelvarrow &amp; North East Valley<br>Brightwater Doctors Surgery</p>
    <div class="appt-rows">
      <div class="appt-row">Date<span class="appt-line date"></span>Time<span class="appt-line time"></span>am/pm</div>
      <div class="appt-row">Date<span class="appt-line date"></span>Time<span class="appt-line time"></span>am/pm</div>
      <div class="appt-row">Date<span class="appt-line date"></span>Time<span class="appt-line time"></span>am/pm</div>
    </div>
  </section>

  <section class="card card-contact">
    <div class="side-band"></div>
    <div class="side-band-top"></div>
    <span class="contact-mark"></span>
    <span class="contact-brand-name">Kelvarrow Nutrition &amp; Dietetics</span>
    <div class="person">
      <p class="person-name">Martin Ellacott</p>
      <p class="person-title">Accredited Nutritionist</p>
    </div>

    <svg class="icon" style="left:95px;top:196px" width="14" height="18" viewBox="0 0 14 18" aria-label="Locations">
      <path d="M7 0C3.1 0 0 3 0 6.8 0 11.5 7 18 7 18s7-6.5 7-11.2C14 3 10.9 0 7 0z" fill="#fff"/>
      <circle cx="7" cy="6.8" r="2.6" fill="#1479c9"/>
    </svg>
    <svg class="icon" style="left:94px;top:262px" width="16" height="12" viewBox="0 0 16 12" aria-label="Phone">
      <path d="M1 4c0-2 3-3 7-3s7 1 7 3v1h-4V3.5H5V5H1z" fill="#fff"/>
      <rect x="3" y="6" width="10" height="6" rx="1" fill="#fff"/>
    </svg>
    <svg class="icon" style="left:94px;top:281px" width="16" height="12" viewBox="0 0 16 12" aria-label="Fax">
      <rect x="4" y="0" width="8" height="4" fill="#fff"/>
      <rect x="1" y="4" width="14" height="6" rx="1" fill="#fff"/>
      <rect x="4" y="8" width="8" height="4" fill="#fff" stroke="#1479c9"/>
    </svg>
    <svg class="icon" style="left:94px;top:299px" width="16" height="12" viewBox="0 0 16 12" aria-label="Email">
      <rect x="0" y="0" width="16" height="12" rx="1" fill="#fff"/>
      <path d="M1 1l7 6 7-6" fill="none" stroke="#1479c9" stroke-width="1.4"/>
    </svg>
    <svg class="icon" style="left:95px;top:317px" width="14" height="14" viewBox="0 0 14 14" aria-label="Website">
      <circle cx="7" cy="7" r="6.5" fill="#fff"/>
      <path d="M1 7h12M7 1c-3 3-3 9 0 12M7 1c3 3 3 9 0 12" fill="none" stroke="#1479c9" stroke-width="1"/>
    </svg>

    <div class="details">
      <div class="group">
        Hollins Medical Centre<br>
        Tarrow Medical<br>
        West Feldon Health<br>
        Brightwater Doctors Surgery
      </div>
      <div class="group">
        0400 555 182<br>
        +613 5550 4417<br>
        martin@kelvarrowclinic.com.au<br>
        kelvarrowclinic.com.au
      </div>
    </div>
  </section>

</main>
</body>
</html>
```